Organic skincare label - minimalist, earthy, luxe design needed!

I need a label design for a luxury natural skin care line called "Velka Botaniq". Velka means 'earth' in Swahili. I would like the design to embody an earthy feel but be minimalistic and give a luxe vibe. My first product will be a Saffron and Moringa Polish.

The size of the jar is 8oz, label dimensions should be (1.625" Tall x 8.5" Wide)
I will be making other products too such as; oils + toners so I feel free to do labels for glass bottles and/or spray bottles as well.

Forest green, light pinks/nudes/beige, grey, white, gold, are colors that can be used (not all have to be used).

I have included pictures of some things I've worked on myself as well as my original logo design but I need to simplify the logo, no circle around it.
Feel free to get creative.

Thank you! :)
Updates

Target Market(s)

Socially Conscious, Beauty Enthusiast, Minimalist

Industry/Entity Type

Skin Care

Font styles to use
Sans Serif
Other font styles liked:
• "Wonderlove doodle" is the font used for "Velka" in the logo. Feel free to use that or change it as you see fit.

Requirements
Must have
• Simplistic design
would like to stick to a font close to the ones in the logo. Either the one used for the name "Velka" OR the one that the slogan "Soil and Bloom" uses.

I have also included some pictures to capture the aesthetic of my social media and website.

Gender neutral

```html
<!DOCTYPE html>
<html lang="en">
<head>
<meta charset="UTF-8">
<title>Velka Botaniq – Label</title>
<link rel="stylesheet" href="https://fonts.googleapis.com/css2?family=Kaushan+Script&family=Quicksand:wght@400;500&display=swap">
<style>
  :root {
    --backdrop-top: #3c3c3e;
    --backdrop-bottom: #49494b;
    --blush: #dcc1c3;
    --stone: #a7a5a6;
    --paper: #ffffff;
    --ink: #3b3a3b;
    --rose-title: #c9a5a8;
    --leaf-dark: #c4a39e;
    --leaf-light: #dcc3c2;
    --petal-sand: #e1cbae;
    --petal-mist: #d9d9d9;
    --seal: #c8c0a0;
    --seal-ink: #8a6a4a;
    --text-dark: #1e1e1e;
  }
  * { margin: 0; padding: 0; box-sizing: border-box; }
  html, body { width: 1200px; height: 415px; overflow: hidden; }
  body {
    background: linear-gradient(to bottom, var(--backdrop-top) 0, var(--backdrop-top) 214px, var(--backdrop-bottom) 214px);
    font-family: "Quicksand", sans-serif;
    position: relative;
  }
  .label {
    position: absolute;
    left: 68px;
    top: 106px;
    width: 1064px;
    height: 203px;
    display: flex;
    box-shadow: 6px 6px 10px rgba(0,0,0,0.35);
  }
  .panel { position: relative; width: 355px; height: 100%; overflow: hidden; }
  .panel--front { width: 354px; background: var(--paper); }
  .panel--side { background: var(--stone); }
  .band {
    position: absolute; left: 0; top: 0; width: 100%; height: 70px;
    background: var(--blush);
  }
  .floral { position: absolute; z-index: 1; }
  .floral--left {
    left: 0; top: 52px; width: 148px; height: 151px;
    background: radial-gradient(ellipse at 45% 45%, rgba(225,203,174,0.95) 0%, rgba(225,203,174,0.7) 40%, rgba(225,203,174,0) 72%);
  }
  .floral--right {
    left: 218px; top: 0; width: 137px; height: 178px;
    background: radial-gradient(ellipse at 55% 45%, rgba(217,217,217,0.85) 0%, rgba(217,217,217,0.5) 40%, rgba(217,217,217,0) 72%);
  }
  .copy {
    position: absolute;
    z-index: 2;
    font-size: 10px;
    line-height: 12.5px;
    font-weight: 400;
    white-space: nowrap;
  }
  .copy--band { color: var(--ink); }
  .copy--panel { color: var(--paper); }
  .leaf-photo {
    position: absolute; left: 0; top: 0; width: 100%; height: 77px;
    background: linear-gradient(160deg, var(--leaf-light) 0%, var(--leaf-dark) 45%, var(--leaf-light) 100%);
  }
  .seal {
    position: absolute; left: 248px; top: 29px; width: 72px; height: 72px;
    border-radius: 50%;
    background: var(--seal);
    display: flex; align-items: center; justify-content: center;
  }
  .seal__name {
    font-size: 13px;
    font-weight: 500;
    color: var(--seal-ink);
  }
  .product-name {
    position: absolute; left: 23px; top: 92px;
    font-family: "Kaushan Script", cursive;
    font-weight: 400;
    font-size: 34px;
    line-height: 1;
    color: var(--rose-title);
    white-space: nowrap;
  }
  .tagline {
    position: absolute; left: 23px; top: 138px;
    font-size: 21px;
    line-height: 1;
    color: var(--text-dark);
    white-space: nowrap;
  }
  .volume {
    position: absolute; left: 257px; top: 172px;
    font-size: 10px; color: var(--text-dark);
    white-space: nowrap;
  }
</style>
</head>
<body>
  <div class="label">
    <section class="panel panel--side">
      <div class="band"></div>
      <p class="copy copy--band" style="left:26px; top:15px;">
        Lorem ipsum dolor sit amet, consectetuer adipiscing elit, sed<br>
        diam nonummy nibh euismod tincidunt ut laoreet dolore magna.<br>
        Lorem ipsum dolor sit amet, consectetuer adipiscing elit.
      </p>
      <div class="floral floral--left" role="img" aria-label="Line-drawn hibiscus flower illustration in sand tone"></div>
      <p class="copy copy--panel" style="left:130px; top:84px;">
        Lorem ipsum dolor sit amet, consectetuer<br>
        adipiscing elit, sed diam nonummy nibh<br>
        euismod tincidunt ut laoreet dolore magna<br>
        aliquam erat volutpat. Ut wisi enim ad<br>
        minim veniam, quis nostrud exerci tation<br>
        ullamcorper suscipit lobortis nisl ut aliquip<br>
        ex ea commodo consequat.
      </p>
    </section>

    <section class="panel panel--front">
      <div class="leaf-photo" role="img" aria-label="Photograph of dried palm leaves in dusty rose tones"></div>
      <div class="seal"><span class="seal__name">Velka</span></div>
      <h1 class="product-name">Velka Botaniq</h1>
      <p class="tagline">Soil and Bloom</p>
      <p class="volume">1 fl oz / 59mL</p>
    </section>

    <section class="panel panel--side">
      <div class="band"></div>
      <div class="floral floral--right" role="img" aria-label="Line-drawn hibiscus flower illustration in pale grey"></div>
      <p class="copy copy--band" style="left:20px; top:15px;">
        Lorem ipsum dolor sit amet, consectetuer<br>
        adipiscing elit, sed diam nonummy nibh euismod<br>
        tincidunt ut laoreet dolore magna. Lorem ipsum<br>
        dolor sit amet, consectetuer adipiscing elit.
      </p>
      <p class="copy copy--panel" style="left:31px; top:106px;">
        Ingredients: Organic Rosehip<br>
        Seed Oil, Organic Camellia Seed<br>
        Oil, Organic Pomegranate<br>
        Oil, VitaminE Non-GMO
      </p>
      <p class="copy copy--panel" style="left:31px; top:171px;">MADE IN HOUSTON, TX</p>
    </section>
  </div>
</body>
</html>
```